Entrepreneur needs a business card design

I need a business card to name my three companies, as well as contact information.
I'm open on design and color and it can be plain or complex. I'm open on colors but I think I prefer something somewhat formal but fun as well.
I'm open on whether the background is plain or has design in it. I don't have company logos.
Target Market(s)
Auto dealers, realtors and property managers
Industry/Entity Type
Business
Contact Information for Business Card
HOLLISTER FAMILY PROPERTIES, LLC
HOLLISTER PUBLISHING, LLC
LOTMASTER CONSULTING, LLC
Ned Hollister
2847 W. Tamarack Ave. #310
Boise, Idaho 83611-2905
208-514-3092
ned@holl5x.example

```html
<!DOCTYPE html>
<html lang="en">
<head>
<meta charset="utf-8">
<title>Ned Hollister — Business Card</title>
<link rel="stylesheet" href="https://fonts.googleapis.com/css2?family=PT+Sans+Narrow:wght@400;700&display=swap">
<style>
  :root {
    --backdrop: #e6e6e8;
    --card: #f7f7f5;
    --ink-strong: #2f2f2f;
    --ink-soft: #6a6a6a;
    --ink-body: #4a4a4a;
    --accent-red: #e1322a;
    --accent-orange: #f08a2e;
    --corner-grey: #a9a9a9;
    --corner-grey-light: #e2e2e2;
  }
  html, body {
    margin: 0;
    padding: 0;
    width: 1200px;
    height: 900px;
    overflow: hidden;
    background: var(--backdrop);
    font-family: "PT Sans Narrow", "Arial Narrow", sans-serif;
  }
  .stage {
    position: relative;
    width: 1200px;
    height: 900px;
    display: flex;
    align-items: center;
    justify-content: center;
  }
  .card {
    position: relative;
    width: 460px;
    height: 800px;
    background: var(--card);
    box-shadow: 0 2px 10px rgba(0,0,0,0.15);
    overflow: hidden;
  }
  .card-art {
    position: absolute;
    inset: 0;
    width: 460px;
    height: 800px;
  }
  .companies {
    position: absolute;
    top: 56px;
    left: 110px;
    margin: 0;
    padding: 0;
    list-style: none;
    color: var(--ink-soft);
    font-size: 25px;
    line-height: 31px;
    letter-spacing: 0.2px;
    text-transform: uppercase;
  }
  .holder-name {
    position: absolute;
    top: 222px;
    left: 0;
    right: 0;
    margin: 0;
    text-align: center;
    color: var(--ink-strong);
    font-weight: 700;
    font-size: 44px;
    letter-spacing: 0.2px;
  }
  .contact {
    position: absolute;
    top: 500px;
    left: 70px;
    margin: 0;
    color: var(--ink-body);
    font-style: normal;
    font-size: 27px;
    line-height: 34px;
  }
</style>
</head>
<body>
  <main class="stage">
    <section class="card" aria-label="Business card for Ned Hollister">
      <svg class="card-art" viewBox="0 0 460 800" aria-hidden="true">
        <defs>
          <linearGradient id="corner-warm" x1="0" y1="0" x2="1" y2="1">
            <stop offset="0" stop-color="var(--accent-red)"/>
            <stop offset="1" stop-color="var(--accent-orange)"/>
          </linearGradient>
          <linearGradient id="band-warm" x1="0" y1="1" x2="1" y2="0">
            <stop offset="0" stop-color="var(--accent-red)"/>
            <stop offset="0.55" stop-color="var(--accent-orange)"/>
            <stop offset="1" stop-color="var(--accent-orange)"/>
          </linearGradient>
          <linearGradient id="corner-cool" x1="1" y1="1" x2="0" y2="0">
            <stop offset="0" stop-color="var(--corner-grey)"/>
            <stop offset="1" stop-color="var(--corner-grey-light)"/>
          </linearGradient>
        </defs>
        <path class="top-corner" d="M0,0 L190,0 C90,30 20,120 0,250 Z" fill="url(#corner-warm)"/>
        <path class="bottom-corner" d="M460,520 C450,680 380,770 270,800 L460,800 Z" fill="url(#corner-cool)"/>
        <path class="sweep-band" d="M460,300 C458,560 350,740 110,800 L175,800 C370,735 450,590 460,420 Z" fill="url(#band-warm)"/>
      </svg>

      <ul class="companies">
        <li>Hollister Family Properties</li>
        <li>LLC Hollister Publishing</li>
        <li>LLC Lotmaster Consulting</li>
      </ul>

      <h1 class="holder-name">LLC Ned Hollister</h1>

      <address class="contact">
        2847 W. Tamarack Ave.,<br>
        310 Boise, Idaho<br>
        83611-2905, 208-514-3092<br>
        ned@holl5x.example
      </address>
    </section>
  </main>
</body>
</html>
```